New Service Brochure for The Larkmere Spa

Hi All! We are looking for a new brochure design- tri-fold, double sided, and full color. We are a certified Clear Spa for men and women in the heart of the Catskill Mountains of upstate New York. Our clients would describe us as laid back luxury with no pretensions and a home away from home vibe. Our font is Avalon. Key colors are black, white and gold. Looking for an inviting, clean, and modern/minimalist spread with a touch of elegance. No orchid imagery, please. I would like our "Clear Spa" logo on cover, too please. Front cover image with with logo and "Clear Spa" Sticker . Bottom of back with contact info. We would prefer massages go on left inside page, facials in middle and right inside, nails on back left, but we are open to new or different layout proposals. Thank you!

Target Market(s)

Men & Women.

Industry/Entity Type

Health And Wellness

Font styles to use
Other font styles liked:
• Avalon is our signature font

Requirements
Must have
• Easy on the eyes.
Nice to have
• Negative space.
Should not have
• No orchids. Busy lines and wild colors.

```html
<!DOCTYPE html>
<html lang="en">
<head>
<meta charset="utf-8">
<title>The Larkmere Spa – Tri-fold Brochure</title>
<link rel="stylesheet" href="https://fonts.googleapis.com/css2?family=Raleway:wght@300;400;500&display=swap">
<style>
  :root {
    --backdrop: #3a3a3a;
    --paper: #ffffff;
    --paper-soft: #ededed;
    --ink: #2b2b2b;
    --ink-soft: #555555;
    --gold: #d2b06a;
    --gold-deep: #c29a4a;
    --gold-pale: #ead9b0;
    --badge: #4e8a3a;
  }
  * { box-sizing: border-box; margin: 0; padding: 0; }
  html, body { width: 1200px; height: 800px; overflow: hidden; }
  body {
    background: var(--backdrop);
    font-family: "Raleway", Arial, sans-serif;
    color: var(--ink);
    display: flex; align-items: center; justify-content: center;
  }
  .brochure { display: flex; width: 1080px; height: 700px; box-shadow: 0 20px 50px rgba(0,0,0,.45); }
  .panel { position: relative; width: 360px; height: 700px; overflow: hidden; }
  .panel--intro { background: var(--paper); }
  .panel--contact { background: var(--paper-soft); }
  .panel--cover { background: var(--paper-soft); }

  .photo { position: absolute; }
  .wave { position: absolute; left: 0; width: 360px; display: block; }

  /* intro panel */
  .intro__title { position: absolute; left: 34px; top: 46px; font-weight: 300; font-size: 30px; line-height: 1.05; letter-spacing: 1px; }
  .intro__title span { display: block; }
  .intro__title .accent { color: var(--gold); }
  .intro__text { position: absolute; left: 34px; top: 128px; width: 270px; font-size: 11.5px; line-height: 1.45; font-weight: 500; color: var(--ink); }
  .intro__photo { left: 0; top: 250px; width: 360px; height: 300px;
    background: radial-gradient(ellipse at 55% 60%, #4a4a46 0%, #6d6c66 22%, #e8e6df 48%, #f7f6f2 75%); }
  .intro__wave { top: 430px; }
  .intro__closing { position: absolute; left: 34px; top: 570px; width: 300px; font-size: 17px; line-height: 1.4; font-weight: 300; }

  /* contact panel */
  .contact__photo { left: 0; top: 0; width: 360px; height: 340px;
    background: radial-gradient(circle at 50% 55%, #c98c46 0%, #d9a866 30%, #ece6de 55%, #f2f0ec 80%); }
  .contact__wave { top: 250px; }
  .contact__title { position: absolute; top: 378px; width: 100%; text-align: center; font-size: 30px; font-weight: 300; }
  .rule { display: block; margin: 0 auto; }
  .contact__rule { position: absolute; top: 420px; left: 105px; }
  .contact__list { position: absolute; top: 440px; width: 100%; list-style: none; text-align: center; font-size: 12.5px; line-height: 1.5; font-weight: 500; color: var(--ink-soft); }
  .contact__list li { margin-bottom: 8px; }
  .contact__list svg { vertical-align: -2px; margin-right: 5px; }
  .contact__social { position: absolute; top: 640px; left: 0; width: 100%; display: flex; justify-content: center; align-items: center; gap: 10px; }
  .contact__social .line { width: 44px; height: 1px; background: var(--ink-soft); }
  .contact__social .dot { width: 20px; height: 20px; border-radius: 50%; background: var(--gold-deep); }

  /* cover panel */
  .cover__brand { position: absolute; top: 40px; width: 100%; text-align: center; }
  .cover__name { font-size: 32px; font-weight: 400; letter-spacing: 1px; color: var(--ink); }
  .cover__tagline { margin-top: 6px; font-size: 10.5px; font-weight: 500; color: var(--ink-soft); }
  .cover__photo { left: 60px; top: 125px; width: 300px; height: 230px; border-top-left-radius: 130px 115px;
    background: linear-gradient(120deg, #dcdad6 0%, #f1ddd3 40%, #fbf5f0 70%, #ffffff 100%); }
  .cover__wave { top: 250px; }
  .cover__badge { position: absolute; left: 40px; top: 380px; width: 56px; height: 56px; border-radius: 50%; background: var(--badge); }
  .cover__headline { position: absolute; top: 430px; width: 100%; text-align: center; font-size: 27px; font-weight: 300; line-height: 1.25; }
  .cover__rule { position: absolute; top: 550px; left: 105px; }
  .cover__web { position: absolute; top: 575px; width: 100%; text-align: center; font-size: 12.5px; letter-spacing: 2px; font-weight: 500; }
</style>
</head>
<body>
<main class="brochure">

  <section class="panel panel--intro">
    <h2 class="intro__title"><span>WELLNESS</span><span class="accent">REDEFINED</span></h2>
    <p class="intro__text">We believe the simple luxuries of life and service come with a heartfelt smile, a warm cup of tea, and fresh air. Not to mention wide open spaces, breath-taking views and the number one organic skin care line in the world.</p>
    <div class="photo intro__photo" role="img" aria-label="Photo of smooth black massage stones with a sprig of rosemary and a small bottle of amber oil"></div>
    <svg class="wave intro__wave" viewBox="0 0 360 130" height="130" aria-hidden="true">
      <path d="M0 130 L0 115 C90 118 200 100 360 20 L360 130 Z" fill="var(--gold)"/>
      <path d="M0 130 L0 125 C110 125 230 105 360 50 L360 130 Z" fill="var(--paper)"/>
    </svg>
    <p class="intro__closing">Located in the heart of the Catskill Mountains, our down-to-earth staff, laid back atmosphere, and extraordinary services leave no room for pretenses.</p>
  </section>

  <section class="panel panel--contact">
    <div class="photo contact__photo" role="img" aria-label="Photo of spa items on a wooden tray: stones, bath salt, rose petals and a pink oil bottle"></div>
    <svg class="wave contact__wave" viewBox="0 0 360 100" height="100" aria-hidden="true">
      <path d="M0 100 L0 60 C120 75 240 30 360 0 L360 100 Z" fill="var(--gold)"/>
      <path d="M0 100 L0 85 C130 90 250 50 360 30 L360 100 Z" fill="var(--paper-soft)"/>
    </svg>
    <h2 class="contact__title">Contact Us</h2>
    <svg class="rule contact__rule" width="150" height="10" aria-hidden="true">
      <line x1="0" y1="5" x2="150" y2="5" stroke="var(--gold)" stroke-width="1.5"/>
      <circle cx="75" cy="5" r="3" fill="var(--gold)"/>
    </svg>
    <ul class="contact__list">
      <li>
        <svg width="10" height="13" viewBox="0 0 10 13" aria-hidden="true"><path d="M5 0a4.5 4.5 0 0 0-4.5 4.5C.5 8 5 13 5 13s4.5-5 4.5-8.5A4.5 4.5 0 0 0 5 0z" fill="var(--gold)"/><circle cx="5" cy="4.5" r="1.6" fill="var(--paper-soft)"/></svg><br>
        42 Birchwood Hollow Lane<br>Larkmere, NY 12400<br>Just past Mill Street
      </li>
      <li><svg width="13" height="10" viewBox="0 0 13 10" aria-hidden="true"><rect x=".6" y=".6" width="11.8" height="8.8" fill="none" stroke="var(--gold)" stroke-width="1.2"/><path d="M.6 .6 6.5 5.5 12.4 .6" fill="none" stroke="var(--gold)" stroke-width="1.2"/></svg>Info@TheLarkmereSpa.com</li>
      <li><svg width="12" height="12" viewBox="0 0 12 12" aria-hidden="true"><circle cx="6" cy="6" r="5.4" fill="none" stroke="var(--gold)" stroke-width="1.2"/><path d="M4 3.5l1 1-.6.8c.4.9 1 1.5 1.9 1.9l.8-.6 1 1-.8.9c-2-.4-3.8-2.2-4.2-4.2z" fill="var(--gold)"/></svg>(555) 014-2290</li>
      <li><svg width="12" height="12" viewBox="0 0 12 12" aria-hidden="true"><circle cx="6" cy="6" r="5.4" fill="none" stroke="var(--gold)" stroke-width="1.2"/><ellipse cx="6" cy="6" rx="2.3" ry="5.4" fill="none" stroke="var(--gold)" stroke-width="1"/><line x1=".6" y1="6" x2="11.4" y2="6" stroke="var(--gold)" stroke-width="1"/></svg>www.thelarkmerespa.com</li>
    </ul>
    <div class="contact__social" aria-hidden="true">
      <span class="line"></span><span class="dot"></span><span class="dot"></span><span class="dot"></span><span class="line"></span>
    </div>
  </section>

  <section class="panel panel--cover">
    <header class="cover__brand">
      <h1 class="cover__name">The Larkmere Spa</h1>
      <p class="cover__tagline">a boutique spa for Men &amp; Women</p>
    </header>
    <div class="photo cover__photo" role="img" aria-label="Photo of a guest relaxing face down on a white towel during a massage"></div>
    <svg class="wave cover__wave" viewBox="0 0 360 130" height="130" aria-hidden="true">
      <path d="M0 130 L0 90 C120 110 260 90 360 0 L360 130 Z" fill="var(--gold)"/>
      <path d="M0 130 L0 100 C130 120 270 110 360 40 L360 130 Z" fill="var(--paper-soft)"/>
    </svg>
    <div class="cover__badge" role="img" aria-label="Clear Spa certification badge"></div>
    <h2 class="cover__headline">Escape<br>the congestion of<br>everyday life</h2>
    <svg class="rule cover__rule" width="150" height="10" aria-hidden="true">
      <line x1="0" y1="5" x2="150" y2="5" stroke="var(--gold)" stroke-width="1.5"/>
      <circle cx="75" cy="5" r="3" fill="var(--gold)"/>
    </svg>
    <p class="cover__web">www.thelarkmerespa.com</p>
  </section>

</main>
</body>
</html>
```